International Business Consulting Company Website

RV Crestline Advisory is a U.S-based international consulting firm. We combined passion for success in the global business arena with hands-on experience to help foreign companies navigate the entry into U.S. markets and U.S. companies in initiating and expanding exports to foreign markets.

We need a simple 1 page website
Examples of other consultants’ websites:
http://www.falconridgeadvisors.example/#intro
https://www.mtq-advisers.example
http://veronagroup.example
https://harborwiseadvisory.example

I also need the designer to suggest stock images that are suitable (related to international business, exports).

We want our web design to be bold, yet clean and simple.

Target Market(s)

US companies that export abroad, foreign companies that want to do business int he US/ open a subsidiary in the US.

Industry/Entity Type

Business Consultant

Coding

Coded - Design and coding required

Font styles to use
Sans Serif

Requirements
Must have
• Company logo on top

```html
<!DOCTYPE html>
<html lang="en">
<head>
<meta charset="utf-8">
<title>RV Crestline Advisory</title>
<link href="https://fonts.googleapis.com/css2?family=Marcellus&family=Marcellus+SC&display=swap" rel="stylesheet">
<style>
:root{
  --blue:#0d3f8f;
  --blue-bright:#2f5fd6;
  --ink:#1b1b1b;
  --text:#555a60;
  --muted:#8a8f96;
  --line:#e6e8eb;
  --field:#ffffff;
  --field-border:#e1e3e6;
  --night:#0a1226;
  --night-2:#111c38;
  --white:#ffffff;
}
*{box-sizing:border-box;margin:0;padding:0}
html,body{width:1200px;height:3005px;overflow:hidden}
body{font-family:"Marcellus",serif;color:var(--text);background:var(--white);position:relative}
.abs{position:absolute}

/* hero */
.hero{position:absolute;left:0;top:0;width:1200px;height:592px;overflow:hidden}
.hero-photo{position:absolute;inset:0;background:
  radial-gradient(circle at 600px 360px,rgba(255,255,255,.55) 0,rgba(170,200,255,.25) 60px,transparent 180px),
  linear-gradient(180deg,#2c55c9 0%,#3a66d8 45%,#2a4aa6 70%,#1a2440 88%,#232b3c 100%)}
.brand{position:absolute;left:100px;top:50px;display:flex;align-items:center;gap:14px;color:var(--white);font-family:"Marcellus",serif;font-size:34px;letter-spacing:1px}
.brand .mark{width:62px;height:62px;border:2px solid var(--white)}
.nav{position:absolute;top:70px;left:634px;display:flex;align-items:center;font-size:15px;color:var(--white);letter-spacing:.5px}
.nav a{color:var(--white);text-decoration:none;margin-right:48px}
.login{border:1.5px solid var(--white);border-radius:20px;padding:9px 22px;display:flex;align-items:center;gap:6px;font-size:13px;margin-left:-10px}
.hero-name{position:absolute;left:0;width:1200px;top:222px;text-align:center;color:rgba(255,255,255,.45);font-size:74px;letter-spacing:2px}
.hero-title{position:absolute;left:0;width:1200px;top:366px;text-align:center;color:var(--white);font-size:40px;letter-spacing:3px}
.hero-sub{position:absolute;left:0;width:1200px;top:418px;text-align:center;color:var(--white);font-size:27px;letter-spacing:3px}

/* about */
.portrait{position:absolute;left:98px;top:528px;width:250px;height:250px;border-radius:50%;border:4px solid #1a1a1a;background:radial-gradient(circle at 50% 40%,#4a4f58,#15171b)}
.about-title{position:absolute;left:364px;top:628px;font-size:42px;color:var(--ink)}
.about-text{position:absolute;left:364px;top:688px;width:738px;font-size:13.5px;line-height:26px;text-align:right}
.about-text2{position:absolute;left:100px;top:766px;width:1002px;font-size:13.5px;line-height:26px}
.name-link{color:var(--blue)}
.btn{position:absolute;background:var(--blue);color:var(--white);font-size:13px;letter-spacing:.5px;display:flex;align-items:center;justify-content:center;gap:8px}
.read-more{left:102px;top:930px;width:142px;height:42px;border-radius:22px}
.divider{position:absolute;left:98px;top:1050px;width:1004px;height:1px;background:var(--line)}

/* services */
.section-title{position:absolute;left:0;width:1200px;text-align:center;font-size:40px;color:var(--ink)}
.section-rule{position:absolute;left:570px;width:60px;height:3px;background:var(--blue)}
.service-title{position:absolute;font-size:28px;color:var(--ink)}
.service-sub{position:absolute;font-size:14.5px;color:var(--blue);letter-spacing:.3px}
.ticks{position:absolute;list-style:none;font-size:13.5px;line-height:20px}
.ticks li{position:relative;padding-left:34px;margin-bottom:13px}
.ticks svg{position:absolute;left:0;top:4px}
.circle-photo{position:absolute;width:224px;height:224px;border-radius:50%}
.circle-ring{position:absolute;width:250px;height:250px;border-radius:50%;border:2px dotted #b9c3d3}
.port{background:radial-gradient(circle at 50% 70%,#e0a56a 0,#5a5f86 35%,#2c4b8a 70%,#1c2c55 100%)}
.globe{background:radial-gradient(circle at 45% 40%,#4b79d8 0,#1e4aa8 45%,#0b2461 100%)}

/* contact */
.contact-bg{position:absolute;left:0;top:1978px;width:1200px;height:600px;background:linear-gradient(160deg,#f7f7f8 0%,#eeeff1 40%,#f9f9fa 70%,#ececee 100%)}
.field{position:absolute;background:var(--field);border:1px solid var(--field-border);font-size:12px;color:var(--muted);padding:16px 14px}
.field svg{position:absolute;right:12px;top:17px}
.send{left:516px;top:2414px;width:168px;height:48px;font-size:14px}

/* footer */
.footer{position:absolute;left:0;top:2490px;width:1200px;height:515px}
.footer-bg{position:absolute;inset:0;background:linear-gradient(180deg,var(--night-2) 0%,var(--night) 55%,#070c1a 100%)}
.footer-brand{position:absolute;left:100px;top:2596px;display:flex;align-items:center;gap:14px;color:var(--white);font-size:32px;letter-spacing:1px}
.footer-brand .mark{width:62px;height:62px;border:2px solid var(--white)}
.f-head{position:absolute;top:2640px;font-size:21px;color:var(--white);letter-spacing:.5px}
.f-item{position:absolute;font-size:13px;color:#d8dbe2;line-height:24px}
.f-item svg{position:absolute;left:-34px;top:5px}
.f-link{position:absolute;left:750px;font-size:13px;color:#d8dbe2}
.f-link::before{content:"›";color:#5f86d8;margin-right:12px}
.follow{position:absolute;left:966px;top:2694px;display:flex;align-items:center;gap:12px;color:var(--white);font-size:13px}
.follow .dot{width:42px;height:42px;border-radius:50%;border:2px solid var(--white)}
.f-rule{position:absolute;left:100px;top:2906px;width:1000px;height:1px;background:rgba(255,255,255,.25)}
.copy{position:absolute;left:0;width:1200px;top:2934px;text-align:center;font-size:12px;color:#d8dbe2}
</style>
</head>
<body>

<header class="hero">
  <div class="hero-photo" role="img" aria-label="Silhouetted business team around a boardroom table in front of a world map, backlit in blue"></div>
  <div class="brand"><span class="mark"></span>RV CRESTLINE ADVISORY</div>
  <nav class="nav">
    <a href="#">HOME</a><a href="#">SERVICES</a><a href="#">CONTACT US</a>
    <span class="login"><svg width="10" height="11" viewBox="0 0 10 11"><rect x="1" y="5" width="8" height="6" fill="#fff"/><path d="M3 5V3a2 2 0 0 1 4 0v2" stroke="#fff" fill="none" stroke-width="1.4"/></svg>LOG IN</span>
  </nav>
  <div class="hero-name">RV CRESTLINE</div>
  <div class="hero-title">EXPAND YOUR BUSINESS</div>
  <div class="hero-sub">Enter New Markets</div>
</header>

<section class="about">
  <div class="portrait" role="img" aria-label="Portrait photo of the company founder"></div>
  <h2 class="about-title">ABOUT</h2>
  <p class="about-text"><span class="name-link">Mara Kessling</span> has ten years of experience in economic development, foreign direct investment (FDI) and trade. Prior to founding RV Crestline Advisory, she worked as Director of Global Business Development – Europe at the Ridgeway State Development Office (RSDO) assisting European companies to expand in the state.</p>
  <p class="about-text2">While at the RSDO, Mara participated in a number of international trade shows and organized multiple investment and trade missions for the state's governor. Her expertise in international business provides a source of professional advice for the region's firms. She was elected to serve as the RDEC Vice Chair in 2017. Mara is a speaker at the Trade Academy, an RDEC program providing export training and education. She will teach an International Business Management class at Halden State University during the fall semester of 2017.</p>
  <div class="btn read-more">READ MORE <svg width="12" height="12" viewBox="0 0 12 12"><circle cx="6" cy="6" r="6" fill="#fff"/><path d="M5 3.5 7.5 6 5 8.5" stroke="#0d3f8f" stroke-width="1.6" fill="none"/></svg></div>
  <div class="divider"></div>
</section>

<section class="services">
  <h2 class="section-title" style="top:1114px">OUR SERVICES</h2>
  <div class="section-rule" style="top:1178px"></div>

  <h3 class="service-title" style="left:98px;top:1240px">RV CRESTLINE ADVISORY – EXPORTS</h3>
  <p class="service-sub" style="left:98px;top:1290px">ASSISTS U.S. COMPANIES WITH THEIR EXPORT INITIATIVES BY</p>
  <ul class="ticks" style="left:98px;top:1328px;width:650px">
    <li><svg width="14" height="11" viewBox="0 0 14 11"><path d="M1 5.5 5 9.5 13 1" stroke="#0d3f8f" stroke-width="2.4" fill="none"/></svg>Identifying and developing new customer relationships in foreign markets</li>
    <li><svg width="14" height="11" viewBox="0 0 14 11"><path d="M1 5.5 5 9.5 13 1" stroke="#0d3f8f" stroke-width="2.4" fill="none"/></svg>Organizing trade mission trips</li>
    <li><svg width="14" height="11" viewBox="0 0 14 11"><path d="M1 5.5 5 9.5 13 1" stroke="#0d3f8f" stroke-width="2.4" fill="none"/></svg>Coordinating successful trade show visits</li>
    <li><svg width="14" height="11" viewBox="0 0 14 11"><path d="M1 5.5 5 9.5 13 1" stroke="#0d3f8f" stroke-width="2.4" fill="none"/></svg>Providing an assistance with the completion of a strategic export plan</li>
    <li><svg width="14" height="11" viewBox="0 0 14 11"><path d="M1 5.5 5 9.5 13 1" stroke="#0d3f8f" stroke-width="2.4" fill="none"/></svg>Finding additional resources to support and grow companies' exports</li>
    <li><svg width="14" height="11" viewBox="0 0 14 11"><path d="M1 5.5 5 9.5 13 1" stroke="#0d3f8f" stroke-width="2.4" fill="none"/></svg>Connecting companies with other international trade experts to further support their international logistics, payment &amp; financing management, and to address any trade regulations and legal issues</li>
  </ul>
  <div class="circle-ring" style="left:851px;top:1255px"></div>
  <div class="circle-photo port" style="left:864px;top:1268px" role="img" aria-label="Container ship at a lit cargo port at dusk"></div>

  <h3 class="service-title" style="left:444px;top:1626px">RV CRESTLINE ADVISORY – FDI</h3>
  <p class="service-sub" style="left:444px;top:1674px">ASSISTS INTERNATIONAL COMPANIES WITH NAVIGATING THE ENTRY INTO U.S. MARKETS BY</p>
  <ul class="ticks" style="left:444px;top:1708px;width:640px">
    <li><svg width="14" height="11" viewBox="0 0 14 11"><path d="M1 5.5 5 9.5 13 1" stroke="#0d3f8f" stroke-width="2.4" fill="none"/></svg>Managing the site selection process</li>
    <li><svg width="14" height="11" viewBox="0 0 14 11"><path d="M1 5.5 5 9.5 13 1" stroke="#0d3f8f" stroke-width="2.4" fill="none"/></svg>Collecting market data</li>
    <li><svg width="14" height="11" viewBox="0 0 14 11"><path d="M1 5.5 5 9.5 13 1" stroke="#0d3f8f" stroke-width="2.4" fill="none"/></svg>Site identification and analysis</li>
    <li><svg width="14" height="11" viewBox="0 0 14 11"><path d="M1 5.5 5 9.5 13 1" stroke="#0d3f8f" stroke-width="2.4" fill="none"/></svg>Providing an appraisal of proposed incentives and financing assistance</li>
    <li><svg width="14" height="11" viewBox="0 0 14 11"><path d="M1 5.5 5 9.5 13 1" stroke="#0d3f8f" stroke-width="2.4" fill="none"/></svg>Management of the documentation process</li>
  </ul>
  <div class="circle-ring" style="left:111px;top:1645px"></div>
  <div class="circle-photo globe" style="left:124px;top:1658px" role="img" aria-label="Blue globe showing North America"></div>
</section>

<section class="contact">
  <div class="contact-bg" role="img" aria-label="Light grey low-poly background texture"></div>
  <h2 class="section-title" style="top:2044px">CONTACT US</h2>
  <div class="section-rule" style="top:2102px"></div>
  <div class="field" style="left:170px;top:2158px;width:278px;height:46px">Name<svg width="12" height="12" viewBox="0 0 12 12"><circle cx="6" cy="3.5" r="3" fill="#9a9ea4"/><path d="M0.5 12a5.5 5 0 0 1 11 0z" fill="#9a9ea4"/></svg></div>
  <div class="field" style="left:460px;top:2158px;width:280px;height:46px">Email<svg width="13" height="10" viewBox="0 0 13 10"><rect x=".6" y=".6" width="11.8" height="8.8" fill="none" stroke="#9a9ea4" stroke-width="1.2"/><path d="M.6 .6 6.5 5.5 12.4 .6" fill="none" stroke="#9a9ea4" stroke-width="1.2"/></svg></div>
  <div class="field" style="left:752px;top:2158px;width:278px;height:46px">Subject<svg width="12" height="12" viewBox="0 0 12 12"><path d="M1 11 2 8 9 1 11 3 4 10z" fill="#9a9ea4"/></svg></div>
  <div class="field" style="left:170px;top:2226px;width:860px;height:166px">Your Message<svg width="14" height="12" viewBox="0 0 14 12"><ellipse cx="5.5" cy="5" rx="5" ry="4" fill="#9a9ea4"/><ellipse cx="9.5" cy="7.5" rx="4" ry="3.2" fill="#b5b9be"/></svg></div>
  <div class="btn send">SEND MESSAGE</div>
</section>

<footer>
  <div class="footer">
    <div class="footer-bg" role="img" aria-label="Night-time view of a city from above"></div>
    <svg class="abs" style="left:0;top:0" width="1200" height="70" viewBox="0 0 1200 70">
      <path d="M0 0H1200V8Q600 110 0 8Z" fill="#efeff1"/>
      <path d="M0 8Q600 110 1200 8" stroke="#2f5fd6" stroke-width="3" fill="none"/>
    </svg>
  </div>
  <div class="footer-brand"><span class="mark"></span>RV CRESTLINE</div>

  <h4 class="f-head" style="left:456px">CONTACT US</h4>
  <div class="f-item" style="left:492px;top:2682px"><svg width="14" height="13" viewBox="0 0 14 13"><path d="M7 0 14 6H12V13H8.5V9H5.5V13H2V6H0Z" fill="#5f86d8"/></svg>RV Crestline Advisory, LLC<br>Mara Kessling, MBA<br>President</div>
  <div class="f-item" style="left:492px;top:2768px"><svg width="10" height="15" viewBox="0 0 10 15"><rect x=".7" y=".7" width="8.6" height="13.6" rx="1.5" fill="none" stroke="#5f86d8" stroke-width="1.4"/><circle cx="5" cy="12" r=".9" fill="#5f86d8"/></svg>Call Us : +1 (555) 014-2290</div>
  <div class="f-item" style="left:492px;top:2808px"><svg width="14" height="10" viewBox="0 0 14 10"><rect x=".6" y=".6" width="12.8" height="8.8" fill="none" stroke="#5f86d8" stroke-width="1.2"/><path d="M.6 .6 7 5.5 13.4 .6" fill="none" stroke="#5f86d8" stroke-width="1.2"/></svg>info@rvcrestline.example</div>

  <h4 class="f-head" style="left:750px">QUICK LINKS</h4>
  <div class="f-link" style="top:2690px">Home</div>
  <div class="f-link" style="top:2730px">About Us</div>
  <div class="f-link" style="top:2770px">Services</div>
  <div class="f-link" style="top:2810px">Contact Us</div>

  <h4 class="f-head" style="left:966px">FOLLOW US</h4>
  <div class="follow"><span class="dot"></span>ProLink</div>

  <div class="f-rule"></div>
  <p class="copy">© copyright 2017 RV Crestline Advisory . All rights reserved</p>
</footer>

</body>
</html>
```